HollowPine Ventures Inc. Business Card Design

My business is custom renovations and homes.I would need to have a new business logo created to go along with my company name. The business card should be of a modern style as this is the market I am focused on. I would need my contact information and website posted on the card. I would also like to list a few of the tasks I conduct on the card (such as: Renovations, Additions, Repairs, New Homes, Design, Consultations). On the reverse of the card I currently have just my logo and my motto, "Shaping A Bold Path". However, I am open to completely changing everything as I am starting a new year and would like to excel further. Any new ideas and suggestions are always welcomed. Thank you.

Target Market(s)

Upscale residential and commercial renovations and builds

Industry/Entity Type

Business

Contact Information for Business Card

I would like the design to be able to be laser cut or burnt onto a wooden business card. I will be creating one option of cards for really loyal customers (wooden) and a second option for the everyday customer (paper).

Font styles to use
Other font styles liked:
• Calibri / anything of mordern taste

Colors
f37122
5c5c5c
474747
ffffff

Requirements
Must have
• I would like the colours of my business to be a sharp orange and grey. I believe this will symbolize a modern style. I am open to other suggestions if this is not suitable for the designers tastes. My contact info as follows:
• Will Marsh
• President
• HollowPine Ventures Inc.
• 555-214-3987
• will@hollowpineventures.example
• I would like my website (currently under construction) hollowpineventures.example on the card aswell.
Nice to have
• Along with a modern logo representing HollowPine, I would like something on the card besides the logo and contact information. Perhaps a small background design. I feel it may be nice to have my services listed on the card (in smaller font on the bottom) Renovations, Additions, Repairs, Design, Consultations.
Should not have
• The business card should not have too many different colors. Should not have rounded corners.

```html
<!DOCTYPE html>
<html lang="en">
<head>
<meta charset="utf-8">
<title>HollowPine Ventures Inc. — Business Card</title>
<link rel="stylesheet" href="https://fonts.googleapis.com/css2?family=Roboto:wght@400;500;700&display=swap">
<style>
  :root {
    --orange: #f37122;
    --grey-dark: #474747;
    --grey-mid: #5c5c5c;
    --ink: #3a3a3a;
    --white: #ffffff;
    --cream: #fdfbe3;
    --icon-bar: #1f2530;
    --backdrop: #e4e9ed;
  }
  * { margin: 0; padding: 0; box-sizing: border-box; }
  html, body {
    width: 1200px; height: 1192px; overflow: hidden;
    background: var(--backdrop);
    font-family: "Roboto", sans-serif;
  }
  .canvas { position: relative; width: 1200px; height: 1192px; }

  .card {
    position: absolute; left: 224px; width: 749px; height: 432px;
    box-shadow: 0 4px 14px rgba(0,0,0,0.12);
  }
  .card--front { top: 125px; background: var(--cream); }
  .card--back  { top: 637px; background: var(--grey-mid); }

  .holder { position: absolute; left: 83px; top: 72px; }
  .holder__name { font-size: 46px; font-weight: 700; color: var(--grey-dark); letter-spacing: 0.5px; line-height: 1; }
  .holder__title { margin-top: 10px; font-size: 26px; color: var(--orange); }

  .brand-front {
    position: absolute; right: 60px; top: 80px;
    display: flex; flex-direction: column; align-items: flex-end; gap: 10px;
  }
  .brand-front__square { width: 56px; height: 56px; background: var(--orange); }
  .brand-front__name { font-size: 19px; font-weight: 700; color: var(--grey-dark); }

  .icon-bar {
    position: absolute; left: 83px; top: 224px; width: 53px; height: 208px;
    background: var(--icon-bar);
    display: flex; flex-direction: column; justify-content: space-around; align-items: center;
    padding: 14px 0;
  }
  .icon-bar svg { width: 26px; height: 26px; fill: var(--white); }

  .contacts {
    position: absolute; left: 155px; top: 238px;
    display: flex; flex-direction: column; gap: 36px;
    font-size: 24px; color: var(--ink);
  }
  .contacts li { list-style: none; line-height: 30px; }

  .brand-back {
    position: absolute; left: 0; right: 0; top: 120px;
    display: flex; flex-direction: column; align-items: center; gap: 22px;
  }
  .brand-back__square { width: 120px; height: 120px; background: var(--orange); }
  .brand-back__name { font-size: 28px; font-weight: 700; color: var(--white); }

  .services {
    position: absolute; left: 30px; right: 30px; bottom: 30px;
    display: flex; justify-content: space-between;
    font-size: 20px; font-weight: 500; color: var(--white);
  }
  .services li { list-style: none; display: flex; align-items: center; gap: 10px; }
  .services li::before {
    content: ""; width: 18px; height: 18px; border-radius: 50%; background: var(--orange);
  }
</style>
</head>
<body>
<div class="canvas">

  <section class="card card--front">
    <div class="holder">
      <h1 class="holder__name">Will Marsh</h1>
      <p class="holder__title">President</p>
    </div>

    <div class="brand-front">
      <span class="brand-front__square"></span>
      <span class="brand-front__name">HollowPine Ventures Inc.</span>
    </div>

    <div class="icon-bar">
      <svg viewBox="0 0 24 24" aria-label="Phone"><path d="M6.6 10.8a15.1 15.1 0 0 0 6.6 6.6l2.2-2.2a1 1 0 0 1 1-.25 11.4 11.4 0 0 0 3.6.57 1 1 0 0 1 1 1V20a1 1 0 0 1-1 1A17 17 0 0 1 3 4a1 1 0 0 1 1-1h3.5a1 1 0 0 1 1 1c0 1.25.2 2.45.57 3.57a1 1 0 0 1-.25 1z"/></svg>
      <svg viewBox="0 0 24 24" aria-label="Website"><path d="M12 2a10 10 0 1 0 0 20 10 10 0 0 0 0-20zm6.9 6h-3a15.6 15.6 0 0 0-1.4-3.6A8 8 0 0 1 18.9 8zM12 4a14 14 0 0 1 1.9 4h-3.8A14 14 0 0 1 12 4zM4.3 14a8.2 8.2 0 0 1 0-4h3.4a16.5 16.5 0 0 0 0 4zm.8 2h3a15.6 15.6 0 0 0 1.4 3.6A8 8 0 0 1 5.1 16zm3-8h-3a8 8 0 0 1 4.4-3.6A15.6 15.6 0 0 0 8.1 8zM12 20a14 14 0 0 1-1.9-4h3.8A14 14 0 0 1 12 20zm2.3-6H9.7a14.7 14.7 0 0 1 0-4h4.6a14.7 14.7 0 0 1 0 4zm.2 5.6a15.6 15.6 0 0 0 1.4-3.6h3a8 8 0 0 1-4.4 3.6zm1.8-5.6a16.5 16.5 0 0 0 0-4h3.4a8.2 8.2 0 0 1 0 4z"/></svg>
      <svg viewBox="0 0 24 24" aria-label="Email"><path d="M2 5h20v14H2z M3 6l9 7 9-7" fill="none" stroke="#fff" stroke-width="2"/></svg>
    </div>

    <ul class="contacts">
      <li>555-214-3987</li>
      <li>hollowpineventures.example</li>
      <li>will@hollowpineventures.example</li>
    </ul>
  </section>

  <section class="card card--back">
    <div class="brand-back">
      <span class="brand-back__square"></span>
      <span class="brand-back__name">HollowPine Ventures Inc.</span>
    </div>
    <ul class="services">
      <li>Renovations</li>
      <li>Additions</li>
      <li>Repairs</li>
      <li>New Home</li>
      <li>Consultations</li>
    </ul>
  </section>

</div>
</body>
</html>
```